Modern Website For Law Firm Lawyer Melbourne, Australia Coded

We are looking for a modern and sophisticated website design. We would prefer the site to be based on WordPress given it is intuitive and some of our staff have experience using it.

Our law firm is based in Melbourne, Australia and we deal with property. The website must be hosted on a reliable Australian server.

We would also appreciate it if the designer can provide some guidance about how to make changes/upload content, such as photos and articles. We are happy to pay for this advice.

We prefer classic fonts in black or grey. We would also like a dash of colour so please use a green, blue or aqua colour palette that is consistent with our logo attached.

We do not want any law related images - scales of justice, gavel or the like.

Our ultimate goal is to communicate that the firm is professional, affordable, modern, dynamic, knowledgeable and one with the community.

We would like the following pages/sections/icons:

1. Who We Are - we will provide content.

2. Our Services - 1. Property 2. Wills, 3. Powers of Attorney 4. Probate & Estate Administration 5.Consultancy & Agency- we will provide content for each of these sections.

3. Articles - we already have approximately 20 articles on a wordpress blog and would like to port these articles to the website. We can do this ourselves if the designer can give us instructions about how to do this. We would also like to give clients the option to subscribe to our articles.

4. Contact Us - this should include our firms contact details; location map and we would like to give clients the option to "Request A Quote" directly from the page - i.e they will need to provide their full name, phone number email address, choose subject from drop down menu and type a message that gets sent to our outlook email.

5. Terms and Conditions - we will provide content

We really like the style and photographs used in the following website and want something as close to this as possible:

https://www.velbrook.com/

For privacy reasons, we would prefer to provide content together with all business details once we have decided on the winner.

We will monitor entries closely and promise to provide feedback and guidance on each entry.

This project is guaranteed. If our budget is too low please email us so we can discuss further and perhaps increase our budget. We are reasonable in this regard.

Thank you very much for considering this project.

Target Market(s)

General public, professionals, lawyers and conveyancers

Industry/Entity Type

Law Firm

Coding

Coded - Design and coding required

Number of Pages Required

1 page

Font styles to use
Sans Serif

Colors
33b8a4
33a6d7
0692cd
3176b5
00a990
9bcb3c
86cfc6
cadf82
85acd3

Requirements
Must have
• 1. Site must be coded and hosted on a reliable Australian server and it would be much appreciated if the deisgner provides instructions about how to add photos, blog articles etc-
• 2. The site must be secure and have green lock at top of page
• 3. Request A Quote - name, email, phone, drop down subject, message - email to our outlook email
• 4. Article Subscription
• 5. Domain (we have already purchased)
• 6. Location map
• 7. Facebook, LinkedIn, Instagram Icons
• 8. Membership icons in this order - KRT Member > Coastal Female Advocates > Guides From Counsel > Creature Foundation > Dorvo > Malpeth > Kel QR logos attached to go on bottom of page
• 9. Testimonials
Nice to have
• A modern, sophisticated website like:
• https://www.velbrook.com/ - we really like the style of the velbrook photographs
• We also really like this design by Tk of Sketch hive:
• https://www.sketchhive.com.au/design/58201346
Should not have
• Law related images - scales of justice gavel and the like

```html
<!DOCTYPE html>
<html lang="en">
<head>
<meta charset="utf-8">
<title>Ridgeline Lawyers — Melbourne</title>
<link rel="stylesheet" href="https://fonts.googleapis.com/css2?family=Fira+Sans:wght@300;400;500;600&display=swap">
<style>
:root{
  --teal:#33b8a4;
  --teal-soft:#86cfc6;
  --blue:#33a6d7;
  --blue-deep:#0692cd;
  --blue-dark:#3176b5;
  --green:#9bcb3c;
  --ink:#222;
  --text:#666;
  --line:#d9d9d9;
  --footer:#545454;
  --field:#464646;
  --white:#fff;
}
*{box-sizing:border-box;margin:0;padding:0}
html,body{width:1200px;height:2695px;overflow:hidden;background:var(--white)}
body{position:relative;font-family:"Fira Sans",Arial,sans-serif;color:var(--text)}
.abs{position:absolute}

/* header */
.site-header{position:absolute;left:0;top:0;width:1200px;height:75px;background:var(--white)}
.brand{position:absolute;left:162px;top:18px;display:flex;align-items:center;gap:10px}
.brand-mark{width:36px;height:36px;border-radius:50%;background:var(--teal)}
.brand-name{font-size:15px;font-weight:500;color:#3a3a3a;line-height:17px;text-transform:uppercase;letter-spacing:.5px}
.main-nav{position:absolute;left:544px;top:31px;display:flex;gap:0}
.main-nav a{position:absolute;white-space:nowrap;font-size:10.5px;color:#444;text-decoration:none;text-transform:uppercase;letter-spacing:.4px}
.main-nav a.active{font-weight:600;color:#222}
.main-nav a.active::after{content:"";position:absolute;left:0;right:0;top:17px;height:2px;background:#222}
.btn-quote{position:absolute;left:918px;top:20px;width:120px;height:36px;border:2px solid var(--teal);color:var(--teal);font-size:11px;font-weight:500;display:flex;align-items:center;justify-content:center}
.header-strip{position:absolute;left:0;top:73px;width:1200px;height:3px;background:linear-gradient(90deg,var(--green),var(--teal) 30%,var(--blue) 60%,var(--blue-dark))}

/* hero */
.hero{position:absolute;left:0;top:76px;width:1200px;height:316px;background:linear-gradient(180deg,#8c8aa6 0%,#c497a6 38%,#e3b3a8 60%,#7f8c9d 85%,#5d6c7c 100%)}
.hero-copy{position:absolute;left:0;top:115px;width:1200px;text-align:center;color:var(--white)}
.hero-copy .kicker{font-size:24px;font-weight:600;letter-spacing:.5px;line-height:28px}
.hero-copy .city{font-size:42px;font-weight:300;letter-spacing:1px;line-height:48px}
.hero-dots{position:absolute;top:283px;left:572px;display:flex;gap:8px}
.hero-dots span{width:9px;height:9px;border-radius:50%;border:1.5px solid var(--white)}
.hero-dots span.on{background:var(--white)}

/* welcome */
.welcome{position:absolute;left:0;top:410px;width:1200px;text-align:center}
.section-title{font-size:25px;font-weight:400;color:var(--ink)}
.welcome p{width:620px;margin:16px auto 0;font-size:11.5px;line-height:19px;color:var(--text)}
.welcome p + p{margin-top:18px}
.btn-outline{position:absolute;display:flex;align-items:center;justify-content:center;border:2px solid var(--teal);color:var(--teal);font-size:10px;font-weight:500}

/* who we are */
.who-frame{position:absolute;left:611px;top:708px;width:438px;height:264px;border:2px solid var(--teal)}
.who-photo{position:absolute;left:585px;top:720px;width:453px;height:275px;background:linear-gradient(135deg,#2a2a2a,#555 55%,#1c1c1c)}
.who-card{position:absolute;left:163px;top:697px;width:453px;height:275px;background:var(--teal);text-align:center;color:var(--white)}
.who-card h2{margin-top:38px;font-size:22px;font-weight:300}
.who-card p{width:330px;margin:16px auto 0;font-size:11px;line-height:19.5px}
.who-card .btn-light{position:absolute;left:158px;top:194px;width:119px;height:36px;border:2px solid var(--white);display:flex;align-items:center;justify-content:center;font-size:10px;font-weight:500}
.dots-deco{position:absolute;border-radius:50%}
.dots-left{left:92px;top:765px;width:70px;height:130px;background:radial-gradient(circle at 100% 50%,rgba(51,166,215,.55),rgba(51,166,215,0) 70%)}
.dots-right{left:1036px;top:1645px;width:70px;height:130px;background:radial-gradient(circle at 0% 50%,rgba(6,146,205,.55),rgba(6,146,205,0) 70%)}

/* services */
.services-title{position:absolute;left:0;top:1019px;width:1200px;text-align:center;font-size:23px}
.service{position:absolute;top:1081px;width:188px;height:264px;border:1px solid var(--line);background:var(--white);text-align:center}
.service.featured{background:var(--teal-soft);border-color:var(--teal)}
.service svg{position:absolute;left:64px;top:22px;width:60px;height:60px}
.service h3{position:absolute;left:0;top:99px;width:100%;font-size:14px;font-weight:400;color:#333;line-height:18px}
.service .dash{position:absolute;left:87px;top:121px;width:14px;height:2px;background:#333}
.service p{position:absolute;left:18px;top:133px;width:150px;font-size:10px;line-height:15px;color:#444}
.service .more{position:absolute;left:0;top:224px;width:100%;font-size:10px;font-weight:600;color:var(--teal)}
.service.featured .more{color:var(--white)}
.service.featured h3,.service.featured p{color:#335}
.service.tall h3{top:90px}
.service.tall .dash{top:130px}
.service.tall p{top:141px}

/* articles */
.articles-frame{position:absolute;left:145px;top:1483px;width:480px;height:290px;border:2px solid var(--blue)}
.articles-photo{position:absolute;left:163px;top:1467px;width:672px;height:290px;background:linear-gradient(100deg,#b08a66,#c9a27c 45%,#a98262 100%)}
.articles-card{position:absolute;left:616px;top:1590px;width:420px;height:233px;background:var(--blue);text-align:center;color:var(--white)}
.articles-card h2{margin-top:25px;font-size:22px;font-weight:400}
.field-blue{position:absolute;left:63px;width:296px;height:36px;background:var(--blue-deep);text-align:left;padding-left:14px;font-size:10px;font-weight:500;line-height:36px;color:var(--white)}
.btn-subscribe{position:absolute;left:63px;top:174px;width:296px;height:36px;border:2px solid var(--white);font-size:10px;font-weight:500;line-height:32px}

/* map */
.map{position:absolute;left:0;top:1879px;width:1200px;height:372px;background:linear-gradient(180deg,#e3e3e3,#d8d8d8)}
.map-popup{position:absolute;left:449px;top:2047px;width:305px;height:46px;background:var(--white);font-size:10.5px;color:#333;padding:13px 0 0 46px;box-shadow:0 1px 4px rgba(0,0,0,.15)}
.map-popup .close{position:absolute;right:6px;top:-4px;font-size:14px;color:var(--teal);font-weight:600}

/* footer */
.site-footer{position:absolute;left:0;top:2251px;width:1200px;height:444px;background:var(--footer);color:var(--white)}
.site-footer h2{position:absolute;left:162px;top:50px;font-size:23px;font-weight:300}
.field-dark{position:absolute;background:var(--field);font-size:10px;padding:11px 0 0 14px;color:#e6e6e6}
.btn-submit{position:absolute;left:162px;top:353px;width:98px;height:36px;border:2px solid var(--white);font-size:10px;font-weight:500;display:flex;align-items:center;justify-content:center}
.footer-intro{position:absolute;left:770px;top:90px;width:270px;font-size:14.5px;line-height:20.5px;font-weight:300}
.contact-col{position:absolute;top:199px;font-size:10px;line-height:20px}
.contact-col h4{font-size:13px;font-weight:600;margin-bottom:2px}
.copyright{position:absolute;left:770px;top:362px;font-size:9.5px;color:#e6e6e6}
.footer-strip{position:absolute;left:0;bottom:0;width:1200px;height:3px;background:linear-gradient(90deg,var(--green),var(--teal) 30%,var(--blue) 60%,var(--blue-dark))}
</style>
</head>
<body>

<header class="site-header">
  <div class="brand">
    <span class="brand-mark"></span>
    <span class="brand-name">Ridgeline<br>Lawyers</span>
  </div>
  <nav class="main-nav">
    <a class="active" style="left:0">About Us</a>
    <a style="left:63px">Who We Are</a>
    <a style="left:140px">Our Services</a>
    <a style="left:223px">Articles</a>
    <a style="left:282px">Contact Us</a>
  </nav>
  <div class="btn-quote">Quote Request</div>
  <div class="header-strip"></div>
</header>

<section class="hero" role="img" aria-label="City skyline on the waterfront at dusk under a pink sky"></section>
<div class="hero-copy">
  <div class="kicker">OUR LAW FIRM IS BASED IN</div>
  <div class="city">MELBOURNE, AUSTRALIA</div>
</div>
<div class="hero-dots"><span></span><span class="on"></span><span></span><span></span></div>

<section class="welcome">
  <h1 class="section-title">Welcome to Ridgeline Lawyers.</h1>
  <p>Lorem Ipsum has been the industry's standard dummy text ever since the 1500s, when an unknown printer took a galley of type and scrambled it to make a type specimen book.</p>
  <p>Lorem Ipsum has been the industry's standard dummy text ever since the 1500s, when an unknown printer took a galley of type and scrambled it to make a type specimen book. It has survived not only five centuries, but also the leap into electronic typesetting, remaining essentially unchanged. Lorem Ipsum has been the industry's standard dummy text ever since the 1500s, when an unknown printer took a galley of type and scrambled it to make a type specimen book.</p>
</section>
<div class="btn-outline" style="left:541px;top:605px;width:118px;height:36px">Learn More</div>

<div class="dots-deco dots-left" role="img" aria-label="Decorative cluster of blue dots"></div>
<div class="who-frame"></div>
<div class="who-photo" role="img" aria-label="Person in a dark suit giving a thumbs up"></div>
<section class="who-card">
  <h2>Who We Are</h2>
  <p>Lorem Ipsum has been the industry's standard dummy text ever since the 1500s, when an unknown printer took a galley of type and scrambled it to make a type specimen book. It has survived not only five centuries, but also the leap into electronic typesetting, remaining essentially unchanged.</p>
  <div class="btn-light">Read More</div>
</section>

<h2 class="services-title section-title">Our Services</h2>

<article class="service" style="left:65px">
  <svg viewBox="0 0 60 60" fill="none" stroke="#33b8a4" stroke-width="2"><path d="M10 30 L30 12 L50 30"/><path d="M15 26 V50 H45 V26"/><path d="M26 50 V36 H34 V50"/></svg>
  <h3>Property Law</h3><span class="dash"></span>
  <p>Lorem Ipsum has been the industry's standard dummy text ever since the 1500s, when an unknown printer type specimen book.</p>
  <div class="more">Read More &nbsp;›</div>
</article>
<article class="service" style="left:286px">
  <svg viewBox="0 0 60 60" fill="none" stroke="#33b8a4" stroke-width="2"><rect x="6" y="18" width="48" height="20" rx="4"/><circle cx="30" cy="40" r="7"/><path d="M26 46 L24 54 M34 46 L36 54"/></svg>
  <h3>Wills</h3><span class="dash"></span>
  <p>Lorem Ipsum has been the industry's standard dummy text ever since the 1500s, when an unknown printer type specimen book.</p>
  <div class="more">Read More &nbsp;›</div>
</article>
<article class="service" style="left:506px">
  <svg viewBox="0 0 60 60" fill="none" stroke="#33b8a4" stroke-width="2"><rect x="14" y="6" width="32" height="48" rx="2"/><path d="M20 6 V54"/><path d="M26 20 H40 M26 26 H40"/></svg>
  <h3>Powers of Attorney</h3><span class="dash"></span>
  <p>Lorem Ipsum has been the industry's standard dummy text ever since the 1500s, when an unknown printer type specimen book.</p>
  <div class="more">Read More &nbsp;›</div>
</article>
<article class="service featured tall" style="left:727px">
  <svg viewBox="0 0 60 60" fill="none" stroke="#fff" stroke-width="2"><path d="M20 26 V18 A10 10 0 0 1 40 18 V26"/><rect x="14" y="26" width="32" height="26" rx="3"/><circle cx="30" cy="37" r="3"/><path d="M30 40 V45"/></svg>
  <h3>Probate &amp; Estate<br>Administration</h3><span class="dash"></span>
  <p>Industry's standard dummy text ever since the 1500s, when an unknown printer type specimen book.</p>
  <div class="more">Read More &nbsp;›</div>
</article>
<article class="service" style="left:948px">
  <svg viewBox="0 0 60 60" fill="none" stroke="#33b8a4" stroke-width="2"><rect x="32" y="8" width="20" height="16" rx="3"/><path d="M38 24 L36 30 L44 24"/><path d="M24 14 C12 16 8 30 14 40 L18 52 H28"/></svg>
  <h3>Consultancy</h3><span class="dash"></span>
  <p>Lorem Ipsum has been the industry's standard dummy text ever since the 1500s, when an unknown printer type specimen book.</p>
  <div class="more">Read More &nbsp;›</div>
</article>
<div class="btn-outline" style="left:541px;top:1381px;width:118px;height:36px">All More</div>

<div class="articles-frame"></div>
<div class="articles-photo" role="img" aria-label="Wooden desk with glasses, a pen and a notebook"></div>
<section class="articles-card">
  <h2>Our Articles</h2>
  <div class="field-blue" style="top:73px">Name</div>
  <div class="field-blue" style="top:120px">Email</div>
  <div class="btn-subscribe">Subscribe</div>
</section>
<div class="dots-deco dots-right" role="img" aria-label="Decorative cluster of blue dots"></div>

<section class="map" role="img" aria-label="Greyscale street map of the office location"></section>
<div class="map-popup">ABC Street City, 12345 ABC Street City, 12345<span class="close">×</span></div>
<svg class="abs" style="left:592px;top:2103px" width="20" height="28" viewBox="0 0 20 28"><path d="M10 0 C4 0 0 4 0 10 C0 17 10 28 10 28 C10 28 20 17 20 10 C20 4 16 0 10 0Z" fill="#33b8a4"/><circle cx="10" cy="10" r="3.5" fill="#fff"/></svg>

<footer class="site-footer">
  <h2>Contact Us</h2>
  <div class="field-dark" style="left:162px;top:95px;width:255px;height:37px">Full Name</div>
  <div class="field-dark" style="left:427px;top:95px;width:250px;height:37px">Phone Number</div>
  <div class="field-dark" style="left:162px;top:149px;width:255px;height:37px">Email Address</div>
  <div class="field-dark" style="left:427px;top:149px;width:250px;height:37px">Choose Subject</div>
  <div class="field-dark" style="left:162px;top:202px;width:515px;height:128px">Message</div>
  <div class="btn-submit">Submit</div>

  <p class="footer-intro">Lorem Ipsum has been the industry's standard dummy text ever since the 1500s, when an unknown printer took a galley of type and scrambled it to make a type specimen book.</p>
  <div class="contact-col" style="left:770px"><h4>Address</h4>ABC Street City, 12345<br>ABC Street City, 12345</div>
  <div class="contact-col" style="left:921px"><h4>Phone</h4>(000) 000 - 0000<br>(000) 000 - 0000</div>
  <p class="copyright">© Copyright 2018 Ridgeline Lawyers. | All Rights Reserved</p>
  <div class="footer-strip"></div>
</footer>

</body>
</html>
```